Financial services referral site needs a redesign

We need a complete re-brand ; new word press design for our existing site. Need a web 2.0 clean crisp look that will convert highly. Consumers with debt come to our site so we can refer them to 3rd party providers of debt solutions ranging from credit counseling, debt consolidation, refinance and student loan consolidation. I would like to see designs that use the color green and final product should communicate safety, trust and privacy. Show case our A+ ZVQ rating etc. See current site at trellisvalleyhelp.com

- I would like to use light blue color scheme to match the logo. The green is making it look off - I definitely need the lead form to be on the top right side of the page

```html
<!DOCTYPE html>
<html lang="en">
<head>
<meta charset="utf-8">
<title>Trellis Valley Help – Debt Solutions</title>
<link href="https://fonts.googleapis.com/css2?family=Alegreya:ital,wght@0,400;1,400;1,500&family=Alegreya+SC:wght@700&family=Alegreya+Sans:wght@400;500;700;800&display=swap" rel="stylesheet">
<style>
:root{
  --blue-dark:#0a7fc8;
  --blue-mid:#3aa4d6;
  --blue-light:#8ec8d3;
  --orange:#f59a00;
  --ink:#111;
  --grey-text:#777;
  --line:#cfd8dc;
  --panel-top:#ffffff;
  --panel-bottom:#dcedf0;
  --fold:#8a8f92;
}
*{box-sizing:border-box;margin:0;padding:0}
html,body{width:1200px;height:810px;overflow:hidden;background:#fff}
body{font-family:"Alegreya Sans",sans-serif;color:var(--ink);position:relative}
.page{position:relative;width:1200px;height:810px;overflow:hidden}

.site-header{position:absolute;top:0;left:0;width:1200px;height:98px}
.brand{position:absolute;left:75px;top:26px;display:flex;align-items:center;gap:12px}
.brand-mark{width:52px;height:52px;border-radius:50%;background:var(--blue-light)}
.brand-name{font-family:"Alegreya Sans",sans-serif;font-weight:500;font-size:27px;color:var(--blue-dark)}
.main-nav{position:absolute;right:75px;top:37px;display:flex;font-weight:700;font-size:13px}
.main-nav a{color:var(--ink);text-decoration:none;padding:0 10px;border-left:1px solid #999;line-height:14px}
.main-nav a:first-child{border-left:none;color:#aaa}
.main-nav a:last-child{padding-right:0}

.hero{position:absolute;top:98px;left:0;width:1200px;height:385px;background:linear-gradient(180deg,#8ec8d3 0%,#3fa6d8 55%,#0a7fc8 100%)}
.hero-photo{position:absolute;left:75px;top:15px;width:278px;height:370px;background:linear-gradient(180deg,#a8d4df,#5aa9cf);border-radius:120px 120px 0 0}
.hero-copy{position:absolute;left:364px;top:78px;width:320px;color:#fff}
.hero-copy h1{font-weight:800;font-size:42px;line-height:40px;text-transform:uppercase}
.hero-copy p{font-size:17px;line-height:22.5px;margin-top:10px}
.badges{display:flex;gap:4px;margin-top:12px}
.badge{height:37px;border-radius:3px}
.badge-accredited{width:98px;background:#1b5e7d;border:1px solid #fff}
.badge-rating{width:37px;background:#fff;border:1px solid #6e9fb3}

.lead-panel{position:absolute;left:702px;top:80px;width:415px;height:421px;background:linear-gradient(180deg,var(--panel-top),var(--panel-bottom));box-shadow:0 0 4px rgba(0,0,0,.25);text-align:center}
.fold{position:absolute;top:80px;width:8px;height:421px;background:var(--fold)}
.fold-left{left:694px;clip-path:polygon(0 0,100% 0,100% 100%,0 100%,0 96%,100% 100%,100% 0,0 4%)}
.fold-right{left:1117px;clip-path:polygon(0 0,100% 4%,100% 96%,0 100%)}
.lead-panel h2{font-family:"Alegreya SC",serif;font-weight:700;font-size:32px;line-height:28px;color:var(--blue-dark);margin-top:26px}
.lead-panel .lead-intro{font-weight:500;font-size:16.5px;line-height:19px;margin:8px 24px 0}
.lead-form{position:absolute;left:20px;top:135px;width:375px}
.row{display:flex;gap:9px;margin-bottom:10px}
.field{flex:1;height:38px;border:1px solid #222;background:#fff;font-family:"Alegreya",serif;font-style:italic;font-size:14px;color:#999;text-align:left;padding:10px;position:relative}
.field.select::after{content:"";position:absolute;right:10px;top:16px;border-left:6px solid transparent;border-right:6px solid transparent;border-top:8px solid #aaa}
.submit{height:47px;border-radius:8px;background:var(--orange);color:#fff;font-weight:700;font-size:22px;line-height:47px;text-transform:uppercase}
.secure{display:flex;justify-content:center;align-items:center;gap:5px;font-size:13px;margin-top:11px}

.benefits{position:absolute;left:75px;top:550px}
.benefits h2{font-family:"Alegreya SC",serif;font-weight:700;font-size:30px;color:var(--orange);border-bottom:2px solid var(--orange);display:inline-block;line-height:32px}
.benefits ul{list-style:none;margin-top:10px}
.benefits li{display:flex;align-items:center;gap:10px;font-size:20px;height:32px}

.info-card{position:absolute;left:694px;top:558px;width:431px;height:162px;border:1px solid var(--line);border-radius:6px;background:#f7f8f8;text-align:center;padding:12px 14px 0}
.info-card h3{font-family:"Alegreya",serif;font-style:italic;font-weight:500;font-size:18.5px;line-height:22px;color:#666}
.info-card p{font-family:"Alegreya",serif;font-size:15px;line-height:20.5px;letter-spacing:-0.1px;color:var(--grey-text);margin-top:4px}
.info-card a{font-style:italic;font-size:12.5px;color:var(--blue-dark)}

.site-footer{position:absolute;left:0;top:776px;width:1200px;height:34px;border-top:1px solid #bfe0ea;background:linear-gradient(180deg,#fff,#eef6f8);display:flex;justify-content:center;align-items:center;font-size:10.5px;color:#555}
.site-footer span{padding:0 12px;border-left:1px solid #999;line-height:13px}
.site-footer span:first-child{border-left:none}
</style>
</head>
<body>
<div class="page">
  <header class="site-header">
    <div class="brand"><span class="brand-mark"></span><span class="brand-name">Trellis Valley Help</span></div>
    <nav class="main-nav">
      <a href="#">HOME</a><a href="#">DEBT CONSOLIDATION</a><a href="#">ARTICLES</a><a href="#">CLIENTS LOGIN</a>
    </nav>
  </header>

  <section class="hero">
    <div class="hero-photo" role="img" aria-label="Smiling advisor in a dark business suit with arms crossed"></div>
    <div class="hero-copy">
      <h1>Get out of debt &amp; live better!</h1>
      <p>Since 2006, we have helped thousands of consumers get out of debt. Fill out the free no obligation form and take your first step towards financial freedom and peace of mind.</p>
      <div class="badges">
        <div class="badge badge-accredited" role="img" aria-label="Accreditation badge"></div>
        <div class="badge badge-rating" role="img" aria-label="Rating badge"></div>
      </div>
    </div>
  </section>

  <div class="fold fold-left"></div>
  <div class="fold fold-right"></div>
  <aside class="lead-panel">
    <h2>Our Debt Solutions Can<br>Help You!</h2>
    <p class="lead-intro">Find out how much you can save in minutes. Get a free savings estimate online.</p>
    <div class="lead-form">
      <div class="row"><div class="field">First Name</div><div class="field">Last Name</div></div>
      <div class="row"><div class="field">Phone Number</div></div>
      <div class="row"><div class="field">Email Address</div></div>
      <div class="row"><div class="field select">State</div><div class="field select">Debt Amount</div></div>
      <div class="submit">Get Assistance Now!</div>
      <div class="secure">
        <svg width="12" height="15" viewBox="0 0 12 15"><path d="M3 6V4a3 3 0 0 1 6 0v2" fill="none" stroke="#111" stroke-width="2"/><rect x="0" y="6" width="12" height="9" rx="1" fill="#111"/></svg>
        <span>Your information is 100% secure</span>
      </div>
    </div>
  </aside>

  <section class="benefits">
    <h2>Act Now &amp; Take Advantage of The Benefits</h2>
    <ul>
      <li><svg width="28" height="24" viewBox="0 0 28 24"><path d="M2 13l8 8L26 3l-3-1-13 14-5-5z" fill="#5cb531"/></svg>Reduce high interest credit rates</li>
      <li><svg width="28" height="24" viewBox="0 0 28 24"><path d="M2 13l8 8L26 3l-3-1-13 14-5-5z" fill="#5cb531"/></svg>Stop harassing credit calls</li>
      <li><svg width="28" height="24" viewBox="0 0 28 24"><path d="M2 13l8 8L26 3l-3-1-13 14-5-5z" fill="#5cb531"/></svg>One low monthly payment</li>
      <li><svg width="28" height="24" viewBox="0 0 28 24"><path d="M2 13l8 8L26 3l-3-1-13 14-5-5z" fill="#5cb531"/></svg>No costs unless you save</li>
    </ul>
  </section>

  <article class="info-card">
    <h3>When to consider a debt consolidation program?</h3>
    <p>In today’s economy, it is very common for consumer’s to find themselves overwhelmed by credit card debt and in need of debt reduction. Consumers who need more than basic budgeting to pay off debts and are having difficulties making their monthly payments should consider a debt consolidation… <a href="#">read more »</a></p>
  </article>

  <footer class="site-footer">
    <span>© 2014 Trellis Valley Help.</span>
    <span>PH: 800-555-0142</span>
    <span>2280 Harbor Crest Rd #310, Bayview, CA 90000</span>
    <span>Privacy Policy</span>
  </footer>
</div>
</body>
</html>
```